Stationary Design to Complement our Website

We would like template designed for word documents that we can use for headed paper. The template should complement the style of our website & incorporate our existing logo. https://www.velmorantravel.com/

The header and footer design should be sperate PNG or JPEG files that we can copy and paste into word header and footers. They should work on A4 & letter sized papers.

Note the main web colours are as follows:

Black
HEX code #2b2c2b
C=71 M=64 Y=64 K=65
RGB 43,44,43

Green
HEX code #116c49
C=88 M=33 Y=82 K=24
RGB 17,108,73

Current fonts are ALEO & Gilroy.

Fonts and colours in new design don't have to match website exactly but should be complementary.

Font styles to use
Serif

Requirements
Must have
• a simple design that complements our website.
Some kind of graphic on the top & some sort of graphic on the bottom. Not just plain logo on top.
designs that incorporate the clouds might look good
Can also incorporate 5* rate harbor rating
Should not have
• no photographs included on the design

```html
<!DOCTYPE html>
<html lang="en">
<head>
<meta charset="utf-8">
<title>Velmoran Travel Letterhead</title>
<link rel="stylesheet" href="https://fonts.googleapis.com/css2?family=Lato:wght@400&family=Montserrat:wght@400;700&family=Roboto+Condensed:wght@300;400&display=swap">
<style>
  :root {
    --brand-green: #116c49;
    --brand-black: #050607;
    --ink: #2b2c2b;
    --text-grey: #5a5a5a;
    --heading-grey: #5c5c5c;
    --paper: #ffffff;
  }
  html, body {
    margin: 0;
    padding: 0;
    width: 1056px;
    height: 1200px;
    overflow: hidden;
    background: var(--paper);
  }
  .letterhead {
    position: relative;
    width: 1056px;
    height: 1200px;
    background: var(--paper);
    font-family: "Roboto Condensed", sans-serif;
    color: var(--text-grey);
  }
  .brand {
    position: absolute;
    left: 99px;
    top: 62px;
    display: flex;
    align-items: flex-start;
    gap: 14px;
  }
  .brand-dot {
    width: 22px;
    height: 22px;
    border-radius: 50%;
    background: var(--brand-green);
    margin-top: 4px;
  }
  .brand-name {
    font-family: "Montserrat", sans-serif;
    font-weight: 400;
    font-size: 38px;
    line-height: 50px;
    letter-spacing: 9px;
    color: var(--ink);
    text-transform: uppercase;
  }
  .contact {
    position: absolute;
    left: 674px;
    top: 76px;
    height: 70px;
    border-left: 2px solid var(--brand-green);
    padding-left: 28px;
    font-family: "Lato", sans-serif;
    font-size: 21px;
    color: #6b6b6b;
  }
  .contact-row {
    display: flex;
    align-items: center;
    gap: 20px;
    height: 28px;
    margin-top: -7px;
    margin-bottom: 7px;
  }
  .contact-row svg { width: 20px; height: 20px; flex: none; }
  .date {
    position: absolute;
    left: 99px;
    top: 400px;
    font-family: "Montserrat", sans-serif;
    font-size: 19px;
    color: var(--heading-grey);
  }
  .recipient-name {
    position: absolute;
    left: 99px;
    top: 432px;
    margin: 0;
    font-family: "Montserrat", sans-serif;
    font-weight: 700;
    font-size: 30px;
    color: var(--heading-grey);
  }
  .recipient-role {
    position: absolute;
    left: 99px;
    top: 478px;
    font-family: "Montserrat", sans-serif;
    font-size: 19px;
    color: var(--heading-grey);
  }
  .letter-body {
    position: absolute;
    left: 99px;
    top: 552px;
    width: 857px;
    font-size: 19px;
    font-weight: 300;
    line-height: 30px;
    text-align: justify;
  }
  .letter-body p { margin: 0 0 28px; }
  .closing {
    position: absolute;
    left: 99px;
    top: 876px;
    font-size: 20px;
    font-weight: 400;
  }
  .signature {
    position: absolute;
    left: 99px;
    top: 920px;
    width: 110px;
    height: 60px;
    background: linear-gradient(90deg, rgba(17,108,73,0.18), rgba(17,108,73,0.08));
    border-radius: 4px;
  }
  .footer-band {
    position: absolute;
    left: 0;
    top: 1089px;
    width: 1056px;
    height: 65px;
    display: flex;
  }
  .footer-green {
    background: var(--brand-green);
    width: 800px;
    display: flex;
    align-items: center;
  }
  .footer-black { background: var(--brand-black); flex: 1; }
  .address {
    padding-left: 84px;
    font-family: "Lato", sans-serif;
    font-size: 17px;
    color: #ffffff;
  }
  .footer-mark {
    position: absolute;
    left: 760px;
    top: 1074px;
    width: 96px;
    height: 96px;
    border-radius: 50%;
    background: var(--paper);
    display: flex;
    align-items: center;
    justify-content: center;
  }
  .footer-mark span {
    width: 72px;
    height: 72px;
    border-radius: 50%;
    background: var(--brand-green);
  }
</style>
</head>
<body>
<main class="letterhead">
  <header>
    <div class="brand">
      <div class="brand-dot"></div>
      <div class="brand-name">Velmoran<br>Travel</div>
    </div>
    <address class="contact" style="font-style:normal">
      <div class="contact-row">
        <svg viewBox="0 0 24 24" aria-hidden="true"><path fill="#116c49" d="M6.6 10.8a15.2 15.2 0 0 0 6.6 6.6l2.2-2.2c.3-.3.7-.4 1-.2 1.1.4 2.3.6 3.6.6.6 0 1 .4 1 1V20c0 .6-.4 1-1 1A17 17 0 0 1 3 4c0-.6.4-1 1-1h3.5c.6 0 1 .4 1 1 0 1.3.2 2.5.6 3.6.1.3 0 .7-.2 1z"/></svg>
        <span>+353 (0)41 55 20 318</span>
      </div>
      <div class="contact-row">
        <svg viewBox="0 0 24 24" aria-hidden="true"><rect x="2" y="5" width="20" height="14" fill="#116c49"/><path d="M2 5l10 8 10-8M2 19l7-7M22 19l-7-7" stroke="#fff" stroke-width="1.6" fill="none"/></svg>
        <span>hello@velmorantravel.com</span>
      </div>
      <div class="contact-row">
        <svg viewBox="0 0 24 24" aria-hidden="true"><g fill="none" stroke="#116c49" stroke-width="1.5"><circle cx="12" cy="12" r="9"/><ellipse cx="12" cy="12" rx="4" ry="9"/><path d="M3 12h18M4.5 7.5h15M4.5 16.5h15"/></g></svg>
        <span>www.velmorantravel.com</span>
      </div>
    </address>
  </header>

  <div class="date">10 December, 2021</div>
  <h1 class="recipient-name">DANIEL HARTWELL</h1>
  <div class="recipient-role">Cheif Executive Officer</div>

  <section class="letter-body">
    <p>Contrary to popular belief, Lorem Ipsum is not simply random text. It has roots in a piece of classical Latin literature from 45 BC, making it over 2000 years old. Edwin Marlowe, a Latin professor at Ashbury College in Virginia, looked up one of the more obscure Latin words, consectetur.</p>
    <p>Lorem Ipsum comes from sections 1.10.32 and 1.10.33 of "de Finibus Bonorum et Malorum" (The Extremes of Good and Evil) by Aurelian, written in 45 BC. This book is a treatise on the theory of ethics, very popular during the Renaissance. The first line of Lorem Ipsum.</p>
    <p>The standard chunk of Lorem Ipsum used since the 1500s is reproduced below for those interested.</p>
  </section>

  <div class="closing">Best Regards</div>
  <div class="signature" role="img" aria-label="Handwritten signature in green ink"></div>

  <footer>
    <div class="footer-band">
      <div class="footer-green">
        <span class="address">Harbour Lodge, Meadow Lane, Ballyrowan, Co. Clare, Ireland</span>
      </div>
      <div class="footer-black"></div>
    </div>
    <div class="footer-mark" aria-hidden="true"><span></span></div>
  </footer>
</main>
</body>
</html>
```